Stufenfrei Portal
Zielgruppe
Vermittlung von Aufzügen und Treppenliften.
Aufgabenstellung
Wir benötigen ein Design für ein Treppenlift-Portal.
Das Design sollte sehr anprechend & modern sein sowie möchlichst dazu führen, dass der Nutzer gerne seine Nutzerdaten in einem Formular eingibt, um nähere Informationen zu einem gewünschen Treppenlift zu erhalten.
Da die Seite ebenfalls sehr viele Informationen bereitstellt, ist es notwendig, eine horizontale Navigation mit einer ersten & zweiten Ebene zu integrieren.
Da die Interessentengruppe eher 50plus ist, wäre es schön, wenn bei der Designerstellung die Nutzerfreundlichkeit berücksichtigt werden würde.

```html
<!DOCTYPE html>
<html lang="de">
<head>
<meta charset="utf-8">
<title>Stufenfrei Portal</title>
<link rel="stylesheet" href="https://fonts.googleapis.com/css2?family=Arimo:wght@400;700&family=PT+Sans+Narrow:wght@400;700&display=swap">
<style>
:root{
  --teal:#0b7679;
  --teal-dark:#09666a;
  --teal-menu:#12898b;
  --bg:#efefef;
  --panel:#f6f6f6;
  --field:#e6e6e6;
  --rule:#dcdcdc;
  --text:#555;
  --heading:#3a3a3a;
  --white:#fff;
}
*{margin:0;padding:0;box-sizing:border-box}
html,body{width:867px;height:1200px;overflow:hidden}
body{position:relative;background:var(--bg);font-family:"Arimo",Arial,sans-serif;color:var(--text);font-size:8.5px}
.abs{position:absolute}
.cond{font-family:"PT Sans Narrow","Arial Narrow",sans-serif}

/* top bar */
.topline{left:0;top:0;width:867px;height:3px;background:var(--teal)}
.topbar{left:0;top:3px;width:867px;height:27px;background:#e4e4e4;border-bottom:1px solid #d6d6d6}
.toplinks{left:378px;top:12px;font-size:8.5px;color:#444}
.toplinks .current{color:var(--teal)}
.fontsize{left:686px;top:3px;width:89px;height:23px;background:var(--teal);color:var(--white);font-size:10px;text-align:center;line-height:23px;letter-spacing:1px}

/* header */
.brand{left:93px;top:60px;font-size:23px;font-weight:700;color:#555;letter-spacing:.2px}
.slogan{left:179px;top:85px;font-size:11px;color:#555}
.phone-label{left:568px;top:60px;font-size:14px;color:#666}
.phone{left:567px;top:74px;font-size:24px;color:#333}

/* navigation */
.nav{left:92px;top:127px;width:683px;height:26px;background:linear-gradient(#fafafa,#e8e8e8);border-top:1px solid #ddd;border-bottom:1px solid #ccc}
.nav-home{left:92px;top:127px;width:65px;height:26px;display:flex;align-items:center;justify-content:center}
.nav-item{top:134px;font-size:8.7px;color:#555;letter-spacing:.2px}
.nav-active{left:157px;top:125px;width:93px;height:29px;background:var(--teal-dark);color:var(--white);font-size:8.7px;line-height:29px;padding-left:18px}
.sub1{left:157px;top:154px;width:156px}
.sub2{left:313px;top:177px;width:157px}
.sub1 div,.sub2 div{height:24px;line-height:24px;padding-left:18px;color:var(--white);font-size:8.5px;letter-spacing:.2px;border-bottom:1px solid #0c6d70}
.sub1 div{background:var(--teal-menu)}
.sub1 .sel{background:var(--teal-dark)}
.sub2 div{background:var(--teal-menu)}

/* main panel */
.main{left:92px;top:182px;width:484px;height:723px;background:var(--panel);border-bottom:1px solid #ddd}
.h-section{font-size:12px;font-weight:700;color:var(--heading);letter-spacing:.1px}
.rule{height:8px;background:var(--rule)}
.slider{left:103px;top:219px;width:462px;height:295px;background:linear-gradient(110deg,#d9d3cb 0%,#ece7e0 35%,#c9b9a6 65%,#6f5a48 100%)}
.caption{left:299px;top:391px;width:255px;height:71px;background:rgba(240,240,240,.82);text-align:right;padding:11px 14px 0 0;font-size:17px;line-height:21px;color:#222}
.dots{left:299px;top:503px;width:71px;height:20px;background:#f1f1f1;border-radius:0 0 4px 4px;box-shadow:0 2px 3px rgba(0,0,0,.15);display:flex;justify-content:center;align-items:center;gap:8px}
.dots i{width:10px;height:10px;border-radius:50%;background:#555;display:block}
.dots i.off{background:#bbb}
.teaser-img{top:577px;width:220px;height:113px}
.teaser-h{top:700px;font-size:9.5px;font-weight:700;color:#444}
.teaser-p{width:212px;font-size:8px;line-height:12.8px;color:#555}
.benefits{left:103px;top:763px;width:220px}
.benefits .row{height:22.7px;border-top:1px solid #e2e2e2;display:flex;align-items:center;font-size:8.2px;color:#555}
.benefits .cell{width:103px;display:flex;align-items:center;gap:6px;padding-left:13px}

/* sidebar */
.search{left:601px;top:182px;width:170px;height:26px;background:#fafafa;border-bottom:1px solid #ddd;font-size:7.5px;color:#666;padding:9px 0 0 10px}
.info-pack{left:601px;top:222px;width:170px;height:85px;background:linear-gradient(100deg,#e9e6e0,#d8d0c4 60%,#bfb5a8);border:1px solid #ddd;overflow:hidden}
.info-band{position:absolute;right:-26px;top:14px;width:110px;height:17px;background:var(--teal);transform:rotate(45deg);color:var(--white);font-size:8px;text-align:center;line-height:17px}
.catalog{left:601px;top:322px;width:170px;height:242px;background:var(--panel);border-bottom:1px solid #ddd}
.cat-h{left:608px;top:327px;font-size:12px;font-weight:700;color:var(--heading)}
.cat-p{left:608px;top:345px;font-size:7.2px;line-height:10px;color:#555}
.radio{top:382px;font-size:7.2px;color:#444;display:flex;align-items:center;gap:4px}
.radio i{width:7px;height:7px;border-radius:50%;background:#666;display:block}
.radio i.off{background:#e2e2e2}
.field{height:19px;background:var(--field);font-size:7.2px;color:#555;padding:5px 0 0 7px}
.consent{left:614px;top:504px;width:155px;font-size:7.2px;line-height:10px;color:#444;padding-left:14px}
.consent b{letter-spacing:.3px}
.consent svg{position:absolute;left:0;top:2px}
.cta{left:608px;top:533px;width:156px;height:19px;background:var(--teal);color:var(--white);font-size:8.8px;font-weight:700;text-align:center;line-height:19px}
.partner-h{left:601px;top:578px;font-size:7.3px;color:var(--teal)}
.partners{left:601px;top:601px;width:170px;height:65px;background:var(--panel);border-bottom:1px solid #ddd;padding:8px 11px;display:grid;grid-template-columns:1fr 1fr;gap:6px}
.partners i{display:block;background:#dcdcdc;border-radius:2px}

/* footer */
.footer{left:92px;top:934px;width:683px;height:235px;background:#e4e4e4;border-top:1px solid #d3d3d3}
.f-h{top:961px;font-size:12px;font-weight:700;color:var(--heading)}
.f-rule{top:965px;height:8px;background:#c6c6c6}
.f-text{left:103px;top:984px;width:185px;font-size:8px;line-height:12.8px;color:#555}
.f-text p+p{margin-top:7px}
.f-field{left:339px;width:189px;background:#ececec;font-size:8.3px;color:#555;padding:8px 0 0 8px}
.f-note{left:343px;top:1123px;font-size:5.6px;line-height:7.5px;color:#666;letter-spacing:.3px}
.f-btn{left:470px;top:1121px;width:55px;height:19px;background:linear-gradient(#f7f7f7,#e2e2e2);border:1px solid #cfcfcf;border-radius:2px;font-size:7.2px;color:#555;text-align:center;line-height:17px}
.f-contact{left:576px;top:984px;font-size:8.2px;line-height:12.8px;color:#555}
.f-sep{left:574px;top:1049px;width:190px;height:1px;background:#d2d2d2}
.social{top:1059px;width:26px;height:26px;border-radius:50%;background:#555}
.social.accent{background:var(--teal)}
.bottombar{left:0;top:1170px;width:867px;height:30px;background:var(--teal)}
.copyright{left:570px;top:1181px;font-size:7.2px;color:var(--white)}
</style>
</head>
<body>

<div class="abs topline"></div>
<div class="abs topbar"></div>
<div class="abs toplinks"><span class="current">Startseite</span> | Hilfe | Datenschutzbestimmungen | Partner | Kontakt | Impressum</div>
<div class="abs fontsize">A+ A <small>A-</small></div>

<header>
  <div class="abs brand cond">STUFENFREI PORTAL</div>
  <div class="abs slogan cond">Hier könnte Ihr Slogan stehen</div>
  <div class="abs phone-label cond">BERATUNGSTELEFON</div>
  <div class="abs phone cond">+49 (0)4711 28 60 - 10</div>
</header>

<nav>
  <div class="abs nav"></div>
  <div class="abs nav-home">
    <svg width="16" height="14" viewBox="0 0 16 14"><path d="M8 1 L15 7 H13 V13 H9.5 V9 H6.5 V13 H3 V7 H1 Z" fill="#666"/></svg>
  </div>
  <div class="abs nav-active">TREPPENLIFT</div>
  <div class="abs nav-item" style="left:267px">STAIRWALKER</div>
  <div class="abs nav-item" style="left:360px">PRIVATAUFZUG</div>
  <div class="abs nav-item" style="left:455px">PLATTFORMLIFT</div>
  <div class="abs nav-item" style="left:556px">SERVICE</div>
  <div class="abs nav-item" style="left:627px">PARTNER</div>
  <div class="abs nav-item" style="left:701px">KONTAKT</div>
  <div class="abs main"></div>
</nav>

<main>
  <div class="abs h-section cond" style="left:102px;top:193px">HERZLICH W</div>
  <div class="abs rule" style="left:470px;top:196px;width:95px"></div>
  <div class="abs slider" role="img" aria-label="Foto: älteres Paar umarmt sich lächelnd in einem hellen Wohnzimmer"></div>
  <div class="abs caption cond">... damit Sie unbekümmert in die<br>Zukunft blicken können.</div>
  <div class="abs dots"><i></i><i></i><i class="off"></i></div>

  <div class="abs sub1">
    <div>KURVIGE TREPPEN</div>
    <div class="sel">GERADE TREPPEN</div>
    <div>TREPPEN IM AUßENBEREICH</div>
  </div>
  <div class="abs sub2">
    <div>HERSTELLER 1</div>
    <div>HERSTELLER 2</div>
    <div>HERSTELLER 2</div>
    <div>HERSTELLER 2</div>
  </div>

  <div class="abs h-section cond" style="left:102px;top:551px">ÜBERSCHRIFT</div>
  <div class="abs rule" style="left:178px;top:554px;width:387px"></div>

  <div class="abs teaser-img" style="left:103px;background:linear-gradient(100deg,#b79a78,#e6ddd0 55%,#d3c4ae)" role="img" aria-label="Foto: Stairwalker-Gerät vor einer Holztreppe im Wohnraum"></div>
  <div class="abs teaser-img" style="left:345px;background:linear-gradient(100deg,#7a5a44,#d8d2cb 50%,#bdb6ae)" role="img" aria-label="Foto: Treppenlift-Sitz an einer Holztreppe"></div>

  <div class="abs teaser-h" style="left:106px">Die Vorteile auf einen Blick</div>
  <div class="abs teaser-p" style="left:106px;top:715px">Ich bin Blindtext. Von Geburt an. Es hat lange gedauert, bis ich begriffen habe, was es bedeutet, ein blinder Text zu sein: Man macht keinen Sinn.</div>

  <div class="abs teaser-h" style="left:348px">Ich bin eine Überschrift</div>
  <div class="abs teaser-p" style="left:348px;top:715px">Ich bin Blindtext. Von Geburt an. Es hat lange gedauert, bis ich begriffen habe, was es bedeutet, ein blinder Text zu sein: Man macht keinen Sinn.</div>
  <div class="abs teaser-p" style="left:348px;top:760px">Man wirkt hier und da aus dem Zusammenhang gerissen. Oft wird man gar nicht erst gelesen. Aber bin ich deshalb ein schlechter Text? Ich weiß, dass ich nie die Chance haben werde im Stern zu erscheinen. Aber bin ich darum weniger wichtig?</div>
  <div class="abs teaser-p" style="left:348px;top:830px">Ich bin blind! Aber ich bin gerne Text. Und sollten Sie mich jetzt tatsächlich zu Ende lesen, dann habe ich etwas geschafft, was den meisten "normalen" Texten nicht gelingt. Ich bin Blindtext.</div>

  <div class="abs benefits">
    <div class="row"><span class="cell"><svg width="11" height="11" viewBox="0 0 12 12"><circle cx="6" cy="6" r="6" fill="#0b7679"/><path d="M3.2 6.2 L5.2 8.1 L8.9 4.2" stroke="#fff" stroke-width="1.6" fill="none"/></svg>Mobilität</span><span class="cell"><svg width="11" height="11" viewBox="0 0 12 12"><circle cx="6" cy="6" r="6" fill="#0b7679"/><path d="M3.2 6.2 L5.2 8.1 L8.9 4.2" stroke="#fff" stroke-width="1.6" fill="none"/></svg>Sicherheit</span></div>
    <div class="row"><span class="cell"><svg width="11" height="11" viewBox="0 0 12 12"><circle cx="6" cy="6" r="6" fill="#0b7679"/><path d="M3.2 6.2 L5.2 8.1 L8.9 4.2" stroke="#fff" stroke-width="1.6" fill="none"/></svg>Sicherheit</span><span class="cell"><svg width="11" height="11" viewBox="0 0 12 12"><circle cx="6" cy="6" r="6" fill="#0b7679"/><path d="M3.2 6.2 L5.2 8.1 L8.9 4.2" stroke="#fff" stroke-width="1.6" fill="none"/></svg>Lebensqualität</span></div>
    <div class="row"><span class="cell"><svg width="11" height="11" viewBox="0 0 12 12"><circle cx="6" cy="6" r="6" fill="#0b7679"/><path d="M3.2 6.2 L5.2 8.1 L8.9 4.2" stroke="#fff" stroke-width="1.6" fill="none"/></svg>Unabhängigkeit</span><span class="cell"><svg width="11" height="11" viewBox="0 0 12 12"><circle cx="6" cy="6" r="6" fill="#0b7679"/><path d="M3.2 6.2 L5.2 8.1 L8.9 4.2" stroke="#fff" stroke-width="1.6" fill="none"/></svg>Mobilität</span></div>
    <div class="row" style="border-bottom:1px solid #e2e2e2"><span class="cell"><svg width="11" height="11" viewBox="0 0 12 12"><circle cx="6" cy="6" r="6" fill="#0b7679"/><path d="M3.2 6.2 L5.2 8.1 L8.9 4.2" stroke="#fff" stroke-width="1.6" fill="none"/></svg>Lebensqualität</span><span class="cell"><svg width="11" height="11" viewBox="0 0 12 12"><circle cx="6" cy="6" r="6" fill="#0b7679"/><path d="M3.2 6.2 L5.2 8.1 L8.9 4.2" stroke="#fff" stroke-width="1.6" fill="none"/></svg>Unabhängigkeit</span></div>
  </div>
</main>

<aside>
  <div class="abs search">Suchbegriff eingeben...
    <svg style="position:absolute;right:10px;top:8px" width="11" height="11" viewBox="0 0 12 12"><circle cx="4.5" cy="4.5" r="3.4" stroke="#777" stroke-width="1.4" fill="none"/><path d="M7 7 L11 11" stroke="#777" stroke-width="2"/></svg>
  </div>
  <div class="abs info-pack" role="img" aria-label="Foto: Treppe mit Treppenlift, Hinweis auf das Info-Paket"><div class="info-band">Info-Paket</div></div>

  <div class="abs catalog"></div>
  <div class="abs cat-h cond">TREPPENLIFT-KATALOG</div>
  <div class="abs cat-p">Fordern Sie einfach und unkompliziert<br>unser Informationsmaterial an.</div>
  <div class="abs radio" style="left:614px">Herr <i></i></div>
  <div class="abs radio" style="left:673px">Frau <i class="off"></i></div>
  <div class="abs field" style="left:608px;top:397px;width:156px">Name</div>
  <div class="abs field" style="left:608px;top:424px;width:156px">Vorname</div>
  <div class="abs field" style="left:608px;top:450px;width:104px">Straße</div>
  <div class="abs field" style="left:723px;top:450px;width:41px">Nr.</div>
  <div class="abs field" style="left:608px;top:476px;width:40px">PLZ</div>
  <div class="abs field" style="left:660px;top:476px;width:104px">Ort</div>
  <div class="abs consent">
    <svg width="9" height="9" viewBox="0 0 12 12"><circle cx="6" cy="6" r="6" fill="#666"/><path d="M3.2 6.2 L5.2 8.1 L8.9 4.2" stroke="#fff" stroke-width="1.6" fill="none"/></svg>
    Ja, ich habe die Bestimmungen über den <b>Datenschutz</b> gelesen.
  </div>
  <div class="abs cta">kostenlos anfordern</div>

  <div class="abs partner-h">PARTNER</div>
  <div class="abs rule" style="left:644px;top:579px;width:127px;height:7px"></div>
  <div class="abs partners" aria-label="Partner">
    <i></i><i></i><i></i><i></i>
  </div>
</aside>

<footer>
  <div class="abs footer"></div>

  <div class="abs f-h cond" style="left:103px">ÜBERSCHRIFT</div>
  <div class="abs f-rule" style="left:177px;width:115px"></div>
  <div class="abs f-text">
    <p>Ich bin Blindtext. Von Geburt an. Es hat lange gedauert, bis ich begriffen habe, was es bedeutet, ein blinder Text zu sein: Man macht keinen Sinn. Man wirkt hier und da aus dem Zusammenhang gerissen.</p>
    <p>Oft wird man gar nicht erst gelesen. Aber bin ich deshalb ein schlechter Text? Ich weiß, dass ich nie die Chance haben werde im Stern zu erscheinen. Aber bin ich darum weniger wichtig? Ich bin blind!</p>
  </div>

  <div class="abs f-h cond" style="left:338px">KONTAKT</div>
  <div class="abs f-rule" style="left:394px;width:134px"></div>
  <div class="abs f-field" style="top:987px;height:24px">Ihr Name</div>
  <div class="abs f-field" style="top:1019px;height:24px">Ihre@Email.de</div>
  <div class="abs f-field" style="top:1051px;height:65px">Ihre Nachricht an uns</div>
  <div class="abs f-note">Lesen Sie unsere<br>Datenschutzbestimmungen.</div>
  <div class="abs f-btn">abschicken</div>

  <div class="abs f-h cond" style="left:574px">KONTAKTINFORMATIONEN</div>
  <div class="abs f-rule" style="left:709px;width:55px"></div>
  <div class="abs f-contact">Stufenfrei Portal<br>Musterstraße 12, 12345 Musterstadt<br><span style="display:block;height:7px"></span>Tel.: +49 (0) 4711 28 60 - 10<br>FAX: +49 (0) 4711 28 60 - 20</div>
  <div class="abs f-sep"></div>
  <div class="abs social accent" style="left:663px"></div>
  <div class="abs social" style="left:697px"></div>
  <div class="abs social" style="left:731px"></div>

  <div class="abs bottombar"></div>
  <div class="abs copyright">(c) 2012 | Stufenfrei Portal - alle Rechte vorbehalten.</div>
</footer>

</body>
</html>
```